Business card design needed

We need a buisness card design to suit our buisness "Maple Parcel", a company on the south coast of Australia, a wholesale greeting card and gift wrap buisness. We are open to different colour options possibly some pastels. A card that got my attention was'the ''hoofnotes.com.au'' buisness card. I liked the colour scheme, layout, and the use of a cartoon image, but am also open to all ideas.

Industry/Entity Type

Business

Contact Information for Business Card

Maple Parcel Unit 37 / 18 Banksia ave West Torrin 2563 ph 0244879351 fax 0244879352 Colin Madsey email maple.parcel@postvale.com

```html
<!DOCTYPE html>
<html lang="en">
<head>
<meta charset="utf-8">
<title>Maple Parcel – Business Card</title>
<link rel="stylesheet" href="https://fonts.googleapis.com/css2?family=Arimo:ital,wght@0,400;0,700;1,400&display=swap">
<style>
  :root {
    --page: #ffffff;
    --card-light: #4a4a4a;
    --card-mid: #3b3b3b;
    --card-dark: #2c2c2c;
    --ornament: rgba(255, 255, 255, 0.05);
    --text: #ffffff;
    --text-soft: #f0f0f0;
    --accent: #e5702a;
    --footer: #222222;
    --footer-text: #dcdcdc;
  }
  * { margin: 0; padding: 0; box-sizing: border-box; }
  html, body {
    width: 1200px;
    height: 900px;
    overflow: hidden;
    background: var(--page);
    font-family: "Arimo", Arial, sans-serif;
  }
  .card {
    position: absolute;
    left: 375px;
    top: 424px;
    width: 672px;
    height: 373px;
    overflow: hidden;
    background: radial-gradient(ellipse at 50% 40%, var(--card-light) 0%, var(--card-mid) 45%, var(--card-dark) 100%);
    color: var(--text);
  }
  .card__ornament {
    position: absolute;
    left: 0;
    top: 0;
    width: 672px;
    height: 200px;
    background: radial-gradient(ellipse at 65% 30%, var(--ornament) 0%, rgba(255,255,255,0) 70%);
  }
  .identity {
    position: absolute;
    right: 35px;
    top: 37px;
    text-align: right;
  }
  .identity__name {
    font-size: 24px;
    font-weight: 700;
    line-height: 1.2;
  }
  .identity__company {
    font-size: 16.5px;
    font-style: italic;
    line-height: 1.3;
    color: var(--text-soft);
  }
  .identity__tagline {
    font-size: 14px;
    line-height: 1.5;
    color: var(--text-soft);
  }
  .address {
    position: absolute;
    right: 35px;
    top: 189px;
    text-align: right;
    font-size: 19px;
    line-height: 22.5px;
    font-style: normal;
  }
  .contact {
    position: absolute;
    left: 42px;
    top: 240px;
    font-size: 19px;
    line-height: 24.5px;
  }
  .accent-band {
    position: absolute;
    left: 0;
    top: 322px;
    width: 100%;
    height: 19px;
    background: var(--accent);
  }
  .footer {
    position: absolute;
    left: 0;
    top: 341px;
    width: 100%;
    height: 32px;
    background: var(--footer);
  }
  .footer__email {
    position: absolute;
    left: 42px;
    top: 6px;
    font-size: 16.5px;
    color: var(--footer-text);
  }
</style>
</head>
<body>
  <section class="card">
    <div class="card__ornament" role="img" aria-label="Faint swirling flourish pattern across the upper card background"></div>

    <header class="identity">
      <p class="identity__name">Colin Madsey</p>
      <p class="identity__company">Maple Parcel</p>
      <p class="identity__tagline">Greeting Card and Gift Wrap</p>
    </header>

    <address class="address">
      Colin Madsey<br>
      Unit 37 / 18<br>
      Banksia ave West Torrin<br>
      2563
    </address>

    <div class="contact">
      <p class="contact__phone">Phone: 0244879351</p>
      <p class="contact__fax">Fax: 0244879352</p>
    </div>

    <div class="accent-band"></div>
    <footer class="footer">
      <p class="footer__email">maple.parcel@postvale.com</p>
    </footer>
  </section>
</body>
</html>
```